Web Design - RN Fieldline Supply

RN Fieldline Supply is a future eCommerce wholesaler and retailer for tactical equipment such as: bulletproof vests, protective armor plates, ballistic helmets, military uniforms, magazines, military backpacks, etc. our main market will be the U.S market; U.S military, law enforcement and police. You can find the website on www.rnfieldlineshop.com – I’m using a magento template but definitely need to customize the design. A clean and strong design is required and it also needs to incorporate eCommerce color scheme to highlight the important fields; BUY, SHOP, etc.

Please review the attached file to see our logo and incorporate the same style and colors

For exemple:
• http://www.738outfitrow.com/
• http://www.pmwguardworksco.com/
• http://www.tolvanexacta.com/
• http://www.nimbraloftkit.com/
• http://www.vrnopsline.com/
Thanks

Target Market(s)

U.S Military, U.S. Law Enforcement, Police

Industry/Entity Type

Shop

Requirements
Must have
• Home page must have a rotating / revolving banner with U.S Military / U.S Law Enforcement special forces / SWAT / ONQ pictures in battlefield - at least 3-4 banners

```html
<!DOCTYPE html>
<html lang="en">
<head>
<meta charset="utf-8">
<title>RN Fieldline Supply</title>
<link href="https://fonts.googleapis.com/css2?family=Oswald:wght@400;500&family=Ubuntu:wght@400;500&family=Open+Sans:wght@600&family=Arvo:wght@400&display=swap" rel="stylesheet">
<style>
:root{
  --page:#efefef;
  --topbar:#f2f2f2;
  --black:#000;
  --orange:#e08a12;
  --orange-light:#f0a02a;
  --orange-dark:#9a5c08;
  --nav-top:#6a6a6a;
  --nav-bottom:#3a3a3a;
  --tab-top:#dcdcdc;
  --tab-bottom:#a9a9a9;
  --text:#333;
  --white:#fff;
  --line:#cfcfcf;
  --olive:#6b6a45;
  --olive-dark:#3c3d2a;
  --forest:#1c2018;
}
*{box-sizing:border-box;margin:0;padding:0}
html,body{width:1200px;height:900px;overflow:hidden}
body{background:var(--page);font-family:"Ubuntu",sans-serif;color:var(--text);position:relative}
.top-bar{position:absolute;left:0;top:0;width:1200px;height:29px;background:var(--topbar);font-size:12px}
.top-bar .welcome{position:absolute;left:100px;top:7px}
.top-bar .language{position:absolute;right:106px;top:7px}
.top-bar .language b{font-weight:500}
.header{position:absolute;left:0;top:29px;width:1200px;height:116px;background:var(--black)}
.brand{position:absolute;left:96px;top:40px;display:flex;align-items:center;gap:14px}
.brand .mark{width:40px;height:40px;border-radius:50%;background:var(--orange)}
.brand .name{font-size:30px;font-weight:500;color:var(--orange)}
.tab{position:absolute;top:0;height:37px;border-radius:0 0 8px 8px;background:linear-gradient(var(--tab-top),var(--tab-bottom));font-family:"Oswald",sans-serif;font-size:17px;color:#333;text-align:center;line-height:37px}
.tab.login{left:902px;width:96px}
.tab.contacts{left:1002px;width:96px}
.account-links{position:absolute;right:101px;top:51px;display:flex;font-size:12.5px;color:var(--white)}
.account-links span{padding:0 7px;border-left:1px solid var(--white);line-height:13px}
.account-links span:first-child{border-left:none}
.account-links span:last-child{padding-right:0}
.bag{position:absolute;left:797px;top:78px;width:89px;height:38px;border-radius:8px 8px 0 0;background:linear-gradient(#7a7a7a,#555);color:var(--white);font-size:12.5px;text-align:center;line-height:38px}
.search{position:absolute;left:887px;top:76px;width:211px;height:40px;border:2px solid var(--orange);border-bottom:none;border-radius:8px 8px 0 0;background:var(--white);font-size:12px;color:#666;padding:12px 14px}
.search svg{position:absolute;right:8px;top:10px}
.nav-line{position:absolute;left:0;top:145px;width:1200px;height:3px;background:var(--orange)}
.nav{position:absolute;left:0;top:148px;width:1200px;height:50px;background:linear-gradient(var(--nav-top),var(--nav-bottom));display:flex;padding-left:99px}
.nav span{font-family:"Oswald",sans-serif;font-weight:500;font-size:17px;color:var(--white);line-height:50px;padding:0 21px}
.nav span.active{background:linear-gradient(#9a9a9a,#7c7c7c);width:96px;text-align:center;padding:0;margin-right:10px}
.banner{position:absolute;left:96px;top:216px;width:980px;height:421px;
  background:
    radial-gradient(ellipse 22% 45% at 30% 62%, rgba(95,92,58,.95), rgba(95,92,58,0) 100%),
    radial-gradient(ellipse 20% 42% at 62% 60%, rgba(90,88,56,.95), rgba(90,88,56,0) 100%),
    radial-gradient(ellipse 30% 30% at 45% 18%, rgba(170,172,150,.55), rgba(170,172,150,0) 100%),
    linear-gradient(100deg,#55553e 0%,#77775a 30%,#5a5a42 55%,var(--olive-dark) 72%,var(--forest) 100%)}
.banner-panel{position:absolute;left:709px;top:142px;width:271px;height:250px;background:rgba(0,0,0,.9);padding:16px 0 0 20px}
.banner-panel .kicker{font-family:"Open Sans",sans-serif;font-weight:600;font-size:27px;color:var(--orange);line-height:34px}
.banner-panel .title{font-family:"Open Sans",sans-serif;font-weight:600;font-size:45px;color:var(--orange);line-height:50px;letter-spacing:-.5px}
.view-all{position:absolute;left:25px;top:164px;width:175px;height:44px;border-radius:3px;background:linear-gradient(var(--orange-light),#d67a06);font-family:"Open Sans",sans-serif;font-weight:600;font-size:20px;color:var(--white);text-align:center;line-height:44px}
.dots{position:absolute;left:464px;top:398px;display:flex;gap:10px}
.dots i{width:11px;height:11px;background:#ddd}
.dots i.on{background:var(--orange)}
.section-title{position:absolute;left:95px;top:654px;font-family:"Arvo",serif;font-weight:400;font-size:23px;color:var(--orange)}
.card{position:absolute;top:707px;width:220px;height:220px;background:#f4f4f4;border:1px solid #ddd}
.card h3{font-size:14.5px;font-weight:400;text-align:center;margin:8px 10px 0;padding-bottom:6px;border-bottom:1px solid var(--line)}
.card .photo{position:absolute;left:10px;top:50px;width:198px;height:170px;border:1px solid #bbb;background:var(--white)}
.photo.vest{background:radial-gradient(ellipse 38% 60% at 48% 78%,#2a3150 0%,#3a4266 55%,#fff 100%)}
.photo.plate{background:radial-gradient(ellipse 30% 65% at 45% 75%,#111 0%,#2a2a2a 55%,#fff 100%)}
.photo.helmet{background:radial-gradient(ellipse 40% 55% at 45% 72%,#6e6a55 0%,#8c8870 45%,#3a3a36 70%,#fff 100%)}
.photo.uniform{background:
  radial-gradient(ellipse 18% 62% at 30% 75%,#7d8068 0%,#9a9c86 55%,rgba(255,255,255,0) 100%),
  radial-gradient(ellipse 20% 62% at 70% 75%,#3f4a30 0%,#5a6142 55%,rgba(255,255,255,0) 100%),
  #fff}
.card .badge{position:absolute;left:144px;top:60px;width:73px;height:45px;background:var(--orange);color:var(--white);font-family:"Oswald",sans-serif;text-align:center;line-height:1}
.card .badge::after{content:"";position:absolute;right:0;bottom:-7px;border-top:7px solid var(--orange-dark);border-right:7px solid transparent}
.card .badge small{display:block;font-size:14px;font-weight:500;padding-top:3px}
.card .badge b{display:block;font-size:24px;font-weight:500}
</style>
</head>
<body>
<div class="top-bar">
  <span class="welcome">Welcom to rnfieldlineshop.com!</span>
  <span class="language">Select your Language : <b>English</b> ▾</span>
</div>
<header class="header">
  <div class="brand"><span class="mark"></span><span class="name">RN Fieldline Supply</span></div>
  <div class="tab login">LOG IN</div>
  <div class="tab contacts">CONTACTS</div>
  <div class="account-links"><span>My Account</span><span>My Wishlist</span><span>Blog</span><span>FAQ</span><span>Info</span></div>
  <div class="bag">MY BAG 1</div>
  <div class="search">Search
    <svg width="18" height="18" viewBox="0 0 18 18"><circle cx="7" cy="7" r="5" fill="none" stroke="#e08a12" stroke-width="2.5"/><line x1="11" y1="11" x2="16" y2="16" stroke="#e08a12" stroke-width="3" stroke-linecap="round"/></svg>
  </div>
</header>
<div class="nav-line"></div>
<nav class="nav">
  <span class="active">HOME</span><span>ABOUT</span><span>CUSTOMER SERVICE</span><span>SITE MAP</span><span>SEARCH TERMS</span><span>CONTACTS</span>
</nav>
<section class="banner" role="img" aria-label="Special forces team in olive uniforms aiming rifles in a forest">
  <div class="banner-panel">
    <div class="kicker">AUTOMATIC</div>
    <div class="title">WEAPONS</div>
    <div class="view-all">VIEW ALL</div>
  </div>
  <div class="dots"><i></i><i></i><i class="on"></i><i></i></div>
</section>
<h2 class="section-title">Our most popular products &amp; services</h2>
<div class="card" style="left:98px"><h3>Bulletproof Vests</h3><div class="photo vest" role="img" aria-label="Navy police bulletproof vest"></div><div class="badge"><small>You Save</small><b>5%</b></div></div>
<div class="card" style="left:358px"><h3>Protective Armor Plates</h3><div class="photo plate" role="img" aria-label="Black protective armor plate"></div><div class="badge"><small>You Save</small><b>15%</b></div></div>
<div class="card" style="left:618px"><h3>Ballistic Helmets</h3><div class="photo helmet" role="img" aria-label="Tan ballistic helmet with headset"></div><div class="badge"><small>You Save</small><b>8%</b></div></div>
<div class="card" style="left:878px"><h3>Military Uniforms</h3><div class="photo uniform" role="img" aria-label="Two camouflage military uniforms"></div><div class="badge"><small>You Save</small><b>20%</b></div></div>
</body>
</html>
```